Velmora ICT is an ICT Project Services, ICT Architecture and Cloud consultation service business. I need a web site that is simple and looks professional and can grow with my business. I'll leave the creativity and colours up to you as the creative professionals.
Our ICT Project Services specialise in small to medium ICT Projects for government agencies and private organisations and Defence. Our project consultancy services helps our clients get to project execution, Projects as a Service. More information on the offering to be provided.
Cloud services consultation aide and manage in getting clients into the cloud, utilising our technical experience and project management.
I need additional tabs on the site to cater for my additional services.
I am about to offer Quintaris Cloud Certification which will be a paid monthly subscription.
I also require a tab that focuses on our developed Project software. Project as a service. Essentially a step by step application that controls and runs the project from execution to closure for small (complex service requests) projects under $100000.
Happy to provide much more information.
Small to medium business, government agencies
It Company
Velmora ICT
Business Project Management and Architectural Services
Project Management as a Service.
Velmora ICT Consultative Business, Project Management and Architectural Services
2 page
- Additional tabs for the additional products ICT Training and Project Management Applicaiton

```html
<!DOCTYPE html>
<html lang="en">
<head>
<meta charset="utf-8">
<title>Velmora ICT</title>
<link rel="stylesheet" href="https://fonts.googleapis.com/css2?family=Roboto:wght@400;500;700&family=Roboto+Condensed:wght@400;700&display=swap">
<style>
:root{
  --blue:#1f7ac4;
  --blue-deep:#0c54c4;
  --blue-dark:#0e3f7a;
  --blue-mid:#3d74b3;
  --green:#6cb134;
  --green-light:#8cc63f;
  --grey-bg:#f0f0f0;
  --text:#333;
  --muted:#777;
  --footer:#262728;
  --white:#fff;
}
*{margin:0;padding:0;box-sizing:border-box}
html,body{width:1200px;height:3175px;overflow:hidden}
body{position:relative;background:var(--grey-bg);font-family:"Roboto",sans-serif;color:var(--text)}
.abs{position:absolute}
.backdrop{position:absolute;left:0;top:0}

/* header */
.site-header{position:absolute;left:0;top:0;width:1200px;height:95px;background:var(--white);box-shadow:0 1px 4px rgba(0,0,0,.08)}
.logo{position:absolute;left:86px;top:22px;font-family:"Roboto Condensed",sans-serif;font-weight:700;font-size:42px;color:var(--blue);letter-spacing:.5px}
.main-nav{position:absolute;right:88px;top:38px;display:flex;gap:30px;font-size:15px;font-weight:500;color:#222;text-transform:uppercase}
.main-nav .active{color:var(--blue)}

/* hero */
.hero-title{position:absolute;left:0;width:1200px;top:340px;text-align:center;font-family:"Roboto Condensed",sans-serif;font-size:56px;color:var(--white);letter-spacing:.5px}
.hero-sub{position:absolute;left:0;width:1200px;top:430px;text-align:center;font-family:"Roboto Condensed",sans-serif;font-size:31px;color:var(--white)}
.slider-arrow{position:absolute;top:376px;width:36px;height:36px}

/* welcome */
.welcome-title{position:absolute;left:0;width:1200px;top:784px;text-align:center;font-family:"Roboto Condensed",sans-serif;font-size:31px;color:var(--white)}
.welcome-text{position:absolute;left:95px;width:1010px;top:842px;text-align:center;font-size:13.5px;line-height:22px;color:var(--white)}
.welcome-text p+p{margin-top:20px}

/* section titles */
.section-title{position:absolute;left:0;width:1200px;text-align:center;font-family:"Roboto Condensed",sans-serif;font-size:32px;color:#222}
.section-title span{color:var(--blue)}
.section-title.on-blue{color:var(--white)}

/* services */
.service{position:absolute;top:1300px;width:320px;text-align:center}
.service svg{display:block;margin:0 auto}
.service h3{margin-top:30px;font-size:17px;font-weight:500;color:#222;text-transform:uppercase}
.service p{margin:10px auto 0;width:290px;font-size:12.5px;line-height:20px;color:var(--muted)}
.service .more{display:inline-block;margin-top:10px;font-size:13px;color:#222}

/* pricing */
.plan{position:absolute;top:1748px;width:274px;height:362px;background:var(--white);border-radius:4px;overflow:hidden;box-shadow:0 3px 10px rgba(0,0,0,.2)}
.plan-head{height:40px;background:var(--blue-dark);color:var(--white);text-align:center;line-height:40px;font-size:19px;font-weight:500}
.plan-head small{font-size:12px;font-weight:400;margin-left:6px}
.plan-price{position:relative;height:106px;background:var(--blue-mid);color:var(--white);text-align:center}
.plan-price .cur{position:absolute;left:82px;top:18px;font-size:26px}
.plan-price .amt{position:absolute;left:102px;top:6px;font-family:"Roboto Condensed",sans-serif;font-size:80px;line-height:94px}
.plan-price .per{position:absolute;top:55px;font-size:15px}
.plan-price::after{content:"";position:absolute;left:127px;bottom:-10px;border-left:10px solid transparent;border-right:10px solid transparent;border-top:10px solid var(--blue-mid)}
.plan-note{margin-top:24px;text-align:center;color:var(--blue);font-size:14px;line-height:19px}
.plan-list{list-style:none;margin:12px 0 0 30px;font-size:13px;color:#666}
.plan-list li{height:26px;display:flex;align-items:center;gap:10px}
.plan-foot{position:absolute;left:0;bottom:0;width:100%;height:36px;background:var(--blue-dark);color:var(--white);text-align:center;line-height:36px;font-size:17px}
.plan.featured .plan-head,.plan.featured .plan-foot{background:var(--green)}
.plan.featured .plan-price{background:var(--green-light)}
.plan.featured .plan-price::after{border-top-color:var(--green-light)}

/* projects */
.project{position:absolute;top:2368px;width:244px;height:292px}
.project::after{content:"";position:absolute;inset:10px;border:2px solid rgba(255,255,255,.6)}
.project-overlay{position:absolute;inset:0;background:rgba(10,20,10,.45);color:var(--white);text-align:center;padding-top:112px;z-index:1}
.project-overlay h4{font-size:15px;font-weight:500}
.project-overlay p{margin:10px auto 0;width:170px;font-size:12px;line-height:19px}
.project-overlay .view{display:inline-block;margin-top:10px;font-size:15px;text-decoration:underline}

/* footer */
.footer-logo{position:absolute;left:88px;top:2932px;font-family:"Roboto Condensed",sans-serif;font-weight:700;font-size:48px;color:var(--blue)}
.footer-col{position:absolute;top:2886px;color:var(--white)}
.footer-col h5{font-size:17px;font-weight:500;letter-spacing:.5px;margin-bottom:16px}
.footer-col p{font-size:13px;line-height:29px}
.news p{line-height:18px;width:220px}
.news .field{margin-top:14px;width:215px;height:32px;background:var(--white);font-size:12px;color:#888;padding:9px 10px}
.news .btn{margin-top:12px;width:96px;height:30px;background:var(--green);font-size:12px;text-align:center;line-height:30px}
.social{display:flex;align-items:center;gap:16px;height:44px;font-size:13px}
.social i{width:30px;height:30px;border-radius:50%;border:1px solid #aaa;display:inline-block}
.footer-rule{position:absolute;left:88px;top:3094px;width:1024px;height:1px;background:#444}
.copyright{position:absolute;left:0;width:1200px;top:3124px;text-align:center;color:var(--white);font-size:13px}
</style>
</head>
<body>

<svg class="backdrop" width="1200" height="3175" viewBox="0 0 1200 3175">
  <defs>
    <linearGradient id="heroTone" x1="0" y1="0" x2="1" y2="1">
      <stop offset="0" stop-color="#8e9294"/>
      <stop offset=".55" stop-color="#6d7072"/>
      <stop offset="1" stop-color="#4a4c4e"/>
    </linearGradient>
    <linearGradient id="greenTone" x1="0" y1="0" x2="1" y2="1">
      <stop offset="0" stop-color="#5aa32a"/>
      <stop offset="1" stop-color="#7abd3a"/>
    </linearGradient>
    <linearGradient id="blueTone" x1="0" y1="0" x2="1" y2="1">
      <stop offset="0" stop-color="#0b4fc0"/>
      <stop offset=".5" stop-color="#1066d8"/>
      <stop offset="1" stop-color="#0a4fb8"/>
    </linearGradient>
  </defs>
  <polygon points="0,600 1200,600 1200,1016 0,1175" fill="url(#greenTone)"/>
  <polygon points="0,95 1200,95 1200,614 600,751 0,614" fill="url(#heroTone)" role="img" aria-label="Photo of hands working on a laptop over architectural plans"/>
  <polygon points="0,1640 1200,1534 1200,2127 0,2254" fill="url(#blueTone)"/>
  <polygon points="0,2692 600,2836 1200,2692 1200,3175 0,3175" fill="var(--footer)"/>
</svg>

<header class="site-header">
  <div class="logo">VELMORA ICT</div>
  <nav class="main-nav">
    <span class="active">Home</span><span>About Us</span><span>ICT Training</span><span>Project Management</span><span>Cloud Certification</span><span>Contact Us</span>
  </nav>
</header>

<svg class="slider-arrow" style="left:62px" viewBox="0 0 36 36"><circle cx="18" cy="18" r="18" fill="#222"/><path d="M21 11l-7 7 7 7" stroke="#fff" stroke-width="3" fill="none"/></svg>
<svg class="slider-arrow" style="left:1102px" viewBox="0 0 36 36"><circle cx="18" cy="18" r="18" fill="#222"/><path d="M15 11l7 7-7 7" stroke="#fff" stroke-width="3" fill="none"/></svg>

<h1 class="hero-title">VELMORA ICT IN AUSTRALIA</h1>
<p class="hero-sub">Our ICT Project Services specialise in small to medium</p>

<h2 class="welcome-title">WELCOME TO VELMORA ICT</h2>
<div class="welcome-text">
  <p>Lorem Ipsum has been the industry's standard dummy text ever since the 1500s, when an unknown printer took a galley of type and scrambled it to make a type specimen book. It has survived not only five centuries, but also the leap into electronic typesetting, remaining essentially unchanged. It was popularised in the 1960s with the release of Lettrafix sheets containing Lorem Ipsum passages, and more recently with desktop publishing software like Folio Layout including versions of Lorem IpsumLorem Ipsum has been the industry's standard dummy text ever since the 1500s,</p>
  <p>when an unknown printer took a galley of type and scrambled it to make a type specimen book. It has survived not only five centuries, but also the leap into electronic typesetting, remaining essentially unchanged. It was popularised in the 1960s with the release of Lettrafix sheets containing Lorem Ipsum passages, and more recently with desktop publishing software like Folio Layout including versions of Lorem Ipsum</p>
</div>

<h2 class="section-title" style="top:1188px">OUR <span>SERVICES</span></h2>

<div class="service" style="left:90px">
  <svg width="48" height="44" viewBox="0 0 48 44"><rect x="2" y="2" width="44" height="30" rx="3" fill="none" stroke="var(--blue)" stroke-width="4"/><rect x="18" y="33" width="12" height="6" fill="var(--blue)"/><rect x="11" y="39" width="26" height="4" fill="var(--blue)"/></svg>
  <h3>ICT Project Services</h3>
  <p>Ipsum has been the industry's standard dummy text ever since the 1500s, when an unknown printer took a galley of type and scrambled it to make</p>
  <span class="more">Learn More →</span>
</div>
<div class="service" style="left:443px">
  <svg width="48" height="44" viewBox="0 0 48 44"><circle cx="24" cy="9" r="7" fill="var(--blue)"/><circle cx="9" cy="14" r="5.5" fill="var(--blue)"/><circle cx="39" cy="14" r="5.5" fill="var(--blue)"/><path d="M12 42c0-13 5-20 12-20s12 7 12 20z" fill="var(--blue)"/><path d="M0 38c0-10 4-16 9-16 3 0 5 2 6 4-3 4-4 8-4 12z" fill="var(--blue)"/><path d="M48 38c0-10-4-16-9-16-3 0-5 2-6 4 3 4 4 8 4 12z" fill="var(--blue)"/></svg>
  <h3>ICT Architecture</h3>
  <p>Ipsum has been the industry's standard dummy text ever since the 1500s, when an unknown printer took a galley of type and scrambled it to make</p>
  <span class="more">Learn More →</span>
</div>
<div class="service" style="left:790px">
  <svg width="48" height="44" viewBox="0 0 48 44"><path d="M12 36a9 9 0 0 1-1-18 12 12 0 0 1 23-3 10 10 0 0 1 3 21z" fill="var(--blue)"/></svg>
  <h3>Cloud Consultation</h3>
  <p>Ipsum has been the industry's standard dummy text ever since the 1500s, when an unknown printer took a galley of type and scrambled it to make</p>
  <span class="more">Learn More →</span>
</div>

<h2 class="section-title on-blue" style="top:1667px">OUR PRICING</h2>

<div class="plan" style="left:146px">
  <div class="plan-head">BASIC<small>Single user</small></div>
  <div class="plan-price"><span class="cur">$</span><span class="amt">4</span><span class="per" style="left:140px">.95 / mo.</span></div>
  <p class="plan-note">Paid annually or $5.95<br>month to month</p>
  <ul class="plan-list">
    <li><svg width="10" height="9"><path d="M1 4.5l3 3 5-6" stroke="var(--blue)" stroke-width="2" fill="none"/></svg>Quintaris Cloud</li>
    <li><svg width="10" height="9"><path d="M1 4.5l3 3 5-6" stroke="var(--blue)" stroke-width="2" fill="none"/></svg>Dolorem ipsum quia dolor sit</li>
    <li><svg width="10" height="9"><path d="M1 4.5l3 3 5-6" stroke="var(--blue)" stroke-width="2" fill="none"/></svg>Porro quisquam est qui dolorem</li>
  </ul>
  <div class="plan-foot">Sign up »</div>
</div>
<div class="plan featured" style="left:440px">
  <div class="plan-head">PRO<small>Single user</small></div>
  <div class="plan-price"><span class="cur">$</span><span class="amt">8</span><span class="per" style="left:140px">.95 / mo.</span></div>
  <p class="plan-note">Paid annually or $5.95<br>month to month</p>
  <ul class="plan-list">
    <li><svg width="10" height="9"><path d="M1 4.5l3 3 5-6" stroke="var(--green)" stroke-width="2" fill="none"/></svg>Quintaris Cloud</li>
    <li><svg width="10" height="9"><path d="M1 4.5l3 3 5-6" stroke="var(--green)" stroke-width="2" fill="none"/></svg>Dolorem ipsum quia dolor sit</li>
    <li><svg width="10" height="9"><path d="M1 4.5l3 3 5-6" stroke="var(--green)" stroke-width="2" fill="none"/></svg>Porro quisquam est qui dolorem</li>
  </ul>
  <div class="plan-foot">Sign up »</div>
</div>
<div class="plan" style="left:736px">
  <div class="plan-head">TEAM<small>Starting at</small></div>
  <div class="plan-price"><span class="cur" style="left:60px">$</span><span class="amt" style="left:82px">20</span><span class="per" style="left:170px">.95 / mo.</span></div>
  <p class="plan-note">Paid annually or $5.95<br>month to month</p>
  <ul class="plan-list">
    <li><svg width="10" height="9"><path d="M1 4.5l3 3 5-6" stroke="var(--blue)" stroke-width="2" fill="none"/></svg>Quintaris Cloud</li>
    <li><svg width="10" height="9"><path d="M1 4.5l3 3 5-6" stroke="var(--blue)" stroke-width="2" fill="none"/></svg>Dolorem ipsum quia dolor sit</li>
    <li><svg width="10" height="9"><path d="M1 4.5l3 3 5-6" stroke="var(--blue)" stroke-width="2" fill="none"/></svg>Porro quisquam est qui dolorem</li>
  </ul>
  <div class="plan-foot">Sign up »</div>
</div>

<h2 class="section-title" style="top:2285px">OUR <span>PROJECT</span></h2>

<div class="project" style="left:85px;background:linear-gradient(180deg,#1c2a3a,#2f3f2a 70%,#1a2418)" role="img" aria-label="Photo of a modern house at dusk">
  <div class="project-overlay">
    <h4>ICT PROJECT SERVICES</h4>
    <p>Nemo enim ipsam voluptatem quia voluptas sit aspernatur aut odit aut fugit, sed quia</p>
    <span class="view">View More</span>
  </div>
</div>
<div class="project" style="left:345px;background:linear-gradient(180deg,#3a6fb0,#1e3552 55%,#c58a3c)" role="img" aria-label="Photo of glass office towers at night"></div>
<div class="project" style="left:605px;background:linear-gradient(160deg,#9cc3e6,#3c74b4 50%,#1b3d6a)" role="img" aria-label="Photo of glass skyscrapers against the sky"></div>
<div class="project" style="left:861px;background:linear-gradient(180deg,#9aa7b8,#4a5563 55%,#2a2f36)" role="img" aria-label="Photo of a modern office building at dusk"></div>

<div class="footer-logo">VELMORA ICT</div>

<div class="footer-col news" style="left:383px">
  <h5>NEWSLETTERS SIGN UP</h5>
  <p>Sign up for our daily email by entering your information below</p>
  <div class="field">Email address</div>
  <div class="btn">SUBSCRIBE</div>
</div>

<div class="footer-col" style="left:705px">
  <h5>GET IN TOUCH</h5>
  <p>Address : 14 Harlow Lane, Eastgate Marsh,<br>Kv4 2RL</p>
  <p>Phone : 555-014-2873.</p>
  <p>Email : hello@velmora.example</p>
</div>

<div class="footer-col" style="left:982px">
  <h5>FOLLOW US ON</h5>
  <div class="social"><i></i>Linkfeed</div>
  <div class="social"><i></i>Chatter</div>
  <div class="social"><i></i>Pictora</div>
</div>

<div class="footer-rule"></div>
<p class="copyright">Copyright © 2016 . All Rights Reserved</p>

</body>
</html>
```